Transformative School Model Needs a Website. I am easy to work with.

Greetings:
I am creating a K-12 school that is a complete and total re-imagination of what education can be for children, families, communities, and the planet. While we will begin as a K-12 school, I really see it as a complete life cycle education (birth to death). I'm looking for a website to describe my new transformational educational model. I anticipate having 7-8 pages. I have all the copy ready.
I am the Founder. I am easy to work with, an effective communicator, and I’m very good at knowing what I want and providing specific and concrete detail, examples, and direction to make sure I use your time wisely.

```html
<!DOCTYPE html>
<html lang="en">
<head>
<meta charset="utf-8">
<title>Lumen Grove School</title>
<link href="https://fonts.googleapis.com/css2?family=Outfit:wght@400;500;600;700&family=Figtree:wght@400;500;600&display=swap" rel="stylesheet">
<style>
:root{
  --orange:#f7821b;
  --blue:#1f4fb0;
  --blue-dark:#163d91;
  --navy:#0e1833;
  --ink:#1b1f2b;
  --text:#4d5466;
  --soft:#eef1f6;
  --white:#ffffff;
  --line:#e3e7ef;
}
*{box-sizing:border-box;margin:0;padding:0}
html,body{width:1200px;height:5204px;overflow:hidden}
body{font-family:"Figtree",sans-serif;color:var(--text);background:var(--white);position:relative}
h1,h2,h3,h4{font-family:"Outfit",sans-serif;color:var(--ink);font-weight:700}
.abs{position:absolute}
.bar{display:block;width:34px;height:4px;background:var(--orange);border-radius:2px}
.btn{position:absolute;display:inline-flex;align-items:center;gap:8px;height:52px;padding:0 28px;border-radius:4px;background:var(--blue);color:var(--white);font-family:"Outfit",sans-serif;font-weight:600;font-size:15px;text-decoration:none}
.btn svg{width:15px;height:15px}
.ph{position:absolute}

/* top bar & nav */
.topbar{position:absolute;top:0;left:0;width:1200px;height:50px;background:var(--orange);color:var(--white);font-size:15px;font-weight:500}
.topbar .item{position:absolute;top:15px;display:flex;align-items:center;gap:10px}
.topbar .social{position:absolute;top:16px;left:1015px;display:flex;gap:16px}
.topbar .social span{width:16px;height:16px;border-radius:50%;border:2px solid var(--white)}
.topbar .divider{position:absolute;left:985px;top:16px;width:1px;height:18px;background:rgba(255,255,255,.6)}
.nav{position:absolute;top:50px;left:0;width:1200px;height:76px;background:var(--white)}
.nav ul{position:absolute;left:304px;top:28px;display:flex;gap:27px;list-style:none;font-family:"Outfit",sans-serif;font-weight:500;font-size:15px;color:var(--ink)}
.nav li.active{color:var(--orange)}
.brand{position:absolute;left:95px;top:8px;width:150px;height:150px;border-radius:50%;background:var(--white);box-shadow:0 4px 14px rgba(0,0,0,.12);display:flex;align-items:center;justify-content:center;text-align:center;font-family:"Outfit",sans-serif;font-weight:700;font-size:18px;line-height:1.15;color:var(--navy);z-index:3}

/* hero */
.hero{position:absolute;top:126px;left:0;width:1200px;height:562px;background:linear-gradient(180deg,#7d93a8 0%,#6f8a7c 45%,#4f7a3a 75%,#3f6a2c 100%)}
.hero .kids{left:90px;top:20px;width:520px;height:542px;background:linear-gradient(160deg,#a9c7e0,#7fa4c7 60%,#5c86b0);border-radius:6px;opacity:.85}
.hero h1{position:absolute;left:665px;top:92px;font-size:60px;line-height:66px;color:var(--white);width:500px}
.hero .swoosh{position:absolute;left:890px;top:224px}
.hero p{position:absolute;left:665px;top:312px;width:430px;font-size:16px;line-height:28px;color:var(--white)}
.hero .btn{left:665px;top:404px;height:50px;padding:0 26px;font-size:15px}
.slider{position:absolute;left:553px;top:508px;display:flex;align-items:center;gap:12px}
.slider i{width:6px;height:6px;border-radius:50%;background:rgba(255,255,255,.6)}
.slider i.on{background:var(--white);width:8px;height:8px}

/* philosophy */
.philosophy{position:absolute;top:688px;left:0;width:1200px;height:608px;background:var(--soft)}
.philosophy h2{position:absolute;left:92px;top:132px;font-size:36px}
.philosophy .bar{position:absolute;left:92px;top:186px}
.philosophy p{position:absolute;left:92px;top:214px;width:492px;font-size:15.5px;line-height:29px}
.philosophy .btn{left:92px;top:416px}
.scroll-cue{position:absolute;left:570px;top:1272px;width:60px;height:60px;border-radius:50%;background:var(--white);display:flex;align-items:center;justify-content:center;color:var(--blue);z-index:2}

/* about */
.about h2,.center-title{position:absolute;left:0;width:1200px;text-align:center;font-size:36px}
.center-bar{position:absolute;left:583px}
.about .text{position:absolute;left:600px;top:1560px;width:500px;font-size:15.5px;line-height:29px}
.about .text p+p{margin-top:20px}
.checks{list-style:none;margin-top:20px}
.checks li{display:flex;align-items:center;gap:16px;margin-bottom:11px;font-size:15.5px}
.about .btn{left:600px;top:1963px}

/* purpose */
.purpose{position:absolute;top:2158px;left:0;width:1200px;height:542px;background:linear-gradient(180deg,#1e4aa8 0%,#2252b8 60%,#1f4fb0 100%)}
.purpose h2{position:absolute;left:92px;top:90px;font-size:36px;color:var(--white)}
.purpose .bar{position:absolute;left:92px;top:142px}
.purpose p{position:absolute;left:555px;top:92px;width:560px;font-size:16px;line-height:29px;color:var(--white)}
.card{position:absolute;width:327px;height:396px;background:var(--white);border-radius:4px;box-shadow:0 8px 24px rgba(20,40,90,.08);text-align:center}
.card svg.icon{position:absolute;left:131px;top:36px;width:66px;height:66px}
.card h3{position:absolute;top:130px;width:100%;font-size:20px;font-weight:600}
.card .bar{position:absolute;left:147px;top:164px;width:32px;height:3px}
.card p{position:absolute;top:188px;left:28px;width:271px;font-size:15.5px;line-height:29px}
.card .more{position:absolute;left:82px;top:306px;width:163px;height:50px;border-radius:4px;background:#dfe6f3;color:var(--blue);font-family:"Outfit",sans-serif;font-weight:600;font-size:15px;display:flex;align-items:center;justify-content:center;gap:8px}
.donate{position:absolute;left:781px;top:2805px;width:327px;height:396px;border-radius:2px;background:linear-gradient(160deg,#8f6b4a 0%,#5c6f78 55%,#2e4e7e 100%);text-align:center;overflow:hidden}
.donate h3{position:absolute;top:168px;width:100%;font-size:29px;line-height:40px;color:var(--white);font-weight:600}
.donate .badge{position:absolute;left:137px;top:38px;width:54px;height:54px;border-radius:50%;background:var(--white);display:flex;align-items:center;justify-content:center}
.donate .give{position:absolute;left:77px;top:310px;width:174px;height:50px;border-radius:4px;background:var(--orange);color:var(--white);font-family:"Outfit",sans-serif;font-weight:600;font-size:15px;display:flex;align-items:center;justify-content:center;gap:8px}

/* statement */
.statement p{position:absolute;left:300px;top:3384px;width:600px;text-align:center;font-size:16px;line-height:29px}

/* testimonials */
.testimonials{position:absolute;top:4080px;left:0;width:1200px;height:685px;background:var(--soft)}
.testimonials h2{position:absolute;left:92px;top:104px;font-size:36px;line-height:44px}
.testimonials .bar{position:absolute;left:92px;top:200px}
.arrow{position:absolute;top:106px;width:62px;height:62px;border-radius:50%;display:flex;align-items:center;justify-content:center}
.quote{position:absolute;width:497px;height:326px;background:var(--white);border-radius:4px;top:260px}
.quote .mark{position:absolute;right:-6px;top:-42px;font-family:"Outfit",sans-serif;font-weight:700;font-size:150px;line-height:1;color:var(--orange)}
.quote .avatar{position:absolute;left:44px;top:34px;width:78px;height:78px;border-radius:50%}
.quote p{position:absolute;left:44px;top:138px;width:410px;font-size:15.5px;line-height:29px}
.quote h4{position:absolute;left:44px;top:242px;font-size:17px;font-weight:500;color:var(--blue)}
.quote span{position:absolute;left:44px;top:270px;font-size:15px}

/* footer */
.footer{position:absolute;top:4765px;left:0;width:1200px;height:439px;background:var(--navy);color:#cfd5e3}
.footer .mark-name{position:absolute;left:110px;top:108px;width:132px;height:132px;border-radius:50%;border:2px solid #fff;display:flex;align-items:center;justify-content:center;text-align:center;font-family:"Outfit",sans-serif;font-weight:700;font-size:17px;line-height:1.15;color:var(--white)}
.footer .socials{position:absolute;left:92px;top:260px;display:flex;gap:12px}
.footer .socials span{width:50px;height:50px;border-radius:50%;background:var(--orange)}
.footer h4{position:absolute;font-size:20px;font-weight:600;color:var(--white)}
.footer .fbar{position:absolute;width:32px;height:4px;background:var(--orange);border-radius:2px}
.footer ul{position:absolute;list-style:none;font-size:15px}
.footer ul li{height:40px}
.contact{position:absolute;left:882px;font-size:15px;line-height:30px;color:var(--white)}
.contact svg{position:absolute;left:0;top:7px}
.contact div{margin-left:40px}
.copyright{position:absolute;left:0;top:380px;width:1200px;text-align:center;font-size:15px;color:#aeb6c8}
</style>
</head>
<body>

<div class="topbar">
  <div class="item" style="left:393px">
    <svg width="18" height="14" viewBox="0 0 18 14" fill="none" stroke="#fff" stroke-width="1.6"><rect x="1" y="1" width="16" height="12" rx="2"/><path d="M1 2l8 6 8-6"/></svg>
    Email: hello@lumengrove.org
  </div>
  <div class="item" style="left:740px">
    <svg width="16" height="16" viewBox="0 0 24 24" fill="none" stroke="#fff" stroke-width="2"><path d="M22 16.9v3a2 2 0 0 1-2.2 2 19.8 19.8 0 0 1-8.6-3.1 19.5 19.5 0 0 1-6-6A19.8 19.8 0 0 1 2.1 4.2 2 2 0 0 1 4.1 2h3a2 2 0 0 1 2 1.7c.1 1 .4 1.9.7 2.8a2 2 0 0 1-.5 2.1L8 9.8a16 16 0 0 0 6 6l1.3-1.3a2 2 0 0 1 2.1-.4c.9.3 1.8.6 2.8.7a2 2 0 0 1 1.7 2z"/></svg>
    Call us: 555-014-2368
  </div>
  <span class="divider"></span>
  <div class="social" aria-label="Social links"><span></span><span></span><span></span></div>
</div>

<nav class="nav">
  <ul>
    <li class="active">About</li><li>School Foundations</li><li>Curriculum</li><li>Pedagogy</li><li>Outcomes</li><li>Opening</li><li>Testimonials</li><li>Donate</li>
  </ul>
</nav>
<div class="brand">Lumen Grove<br>School</div>

<section class="hero">
  <div class="ph kids" role="img" aria-label="Two smiling children standing back to back in a meadow"></div>
  <h1>Complete life cycle education system</h1>
  <svg class="swoosh" width="180" height="20" viewBox="0 0 180 20"><path d="M4 16 C60 2 120 0 176 10" stroke="#f7821b" stroke-width="4" fill="none" stroke-linecap="round"/></svg>
  <p>Lorem ipsum dolor sit ameto consectetur adipiscing elit sed do eiusmod tempor incididunt ut labore.</p>
  <a class="btn">Go To School Foundation <svg viewBox="0 0 16 16" fill="none" stroke="#fff" stroke-width="1.6"><circle cx="8" cy="8" r="7"/><path d="M5 8h6M8.5 5.5 11 8l-2.5 2.5"/></svg></a>
  <div class="slider">
    <svg width="12" height="20" viewBox="0 0 12 20"><path d="M10 2 2 10l8 8" stroke="#fff" stroke-width="2" fill="none"/></svg>
    <i></i><i class="on"></i><i></i>
    <svg width="12" height="20" viewBox="0 0 12 20"><path d="M2 2l8 8-8 8" stroke="#fff" stroke-width="2" fill="none"/></svg>
  </div>
</section>

<section class="philosophy">
  <h2>Spiritual philosophy</h2>
  <span class="bar"></span>
  <p>Lorem ipsum dolor sit ameto econsectetur adipisicing elit, sed do eiusmod tempor incididunt sedit ut labore et dolore magna aliqua. Ut enimosi ad minim veniam, quis nostrud exercitation ullamco laboris nisi ut aliquip exeai commodo consequat. Duis aute irure dolor in reprehenderit in voluptate velit esse cillum dolore eu fugiat nulla pariatur jantan seduis tem.</p>
  <a class="btn">Read More <svg viewBox="0 0 16 16" fill="none" stroke="#fff" stroke-width="1.6"><circle cx="8" cy="8" r="7"/><path d="M5 8h6M8.5 5.5 11 8l-2.5 2.5"/></svg></a>
  <svg class="abs" style="left:725px;top:95px" width="380" height="420" viewBox="0 0 380 420">
    <path d="M12 100 A190 190 0 0 1 368 100" stroke="#f7821b" stroke-width="8" fill="none" stroke-linecap="round"/>
    <path d="M16 320 A190 190 0 0 0 364 320" stroke="#1f4fb0" stroke-width="8" fill="none" stroke-linecap="round"/>
    <circle cx="190" cy="210" r="178" stroke="#1f4fb0" stroke-width="2" stroke-dasharray="2 5" fill="none"/>
  </svg>
  <div class="ph" role="img" aria-label="Boy kneeling in a sunlit field with hands folded in prayer" style="left:740px;top:130px;width:350px;height:350px;border-radius:50%;background:radial-gradient(circle at 40% 30%,#e9d39a,#b7a05a 45%,#6f7a3a 80%)"></div>
</section>
<div class="scroll-cue"><svg width="12" height="18" viewBox="0 0 12 18"><path d="M6 1v15M1.5 11.5 6 16l4.5-4.5" stroke="#1f4fb0" stroke-width="1.6" fill="none"/></svg></div>

<section class="about">
  <h2 style="top:1412px">About me</h2>
  <span class="bar center-bar" style="top:1460px"></span>
  <div class="ph" role="img" aria-label="Green mountain landscape under a blue sky" style="left:0;top:1518px;width:185px;height:314px;border-radius:0 8px 0 0;background:linear-gradient(180deg,#7fb3df 0%,#a7c9e2 30%,#5f9a4c 55%,#3c6e2e 100%)"></div>
  <div class="abs" style="left:215px;top:1872px;width:300px;height:183px;border:5px solid var(--orange);border-radius:4px"></div>
  <div class="ph" role="img" aria-label="Portrait of the founder smiling with arms crossed in an office" style="left:92px;top:1576px;width:382px;height:436px;border-radius:6px;background:linear-gradient(180deg,#e6e8ec 0%,#c9ccd3 60%,#9aa3b2 100%);box-shadow:0 10px 30px rgba(0,0,0,.12)"></div>
  <div class="text">
    <p>Voluptatem accusantium doloremque laudantium, totam rem aperiam, eaque ipsa quae abist illo inventore veritatis et quasi architecto beatae vitae dictaphon sunt explicabo. Nemo enim ipsam voluptatem quia voluptas sit aspernatur auts onno.</p>
    <p>Neque porro quisquam est, qui dolorem ipsum quia dolor sit amet, consectetur, adipisci velit, sed quia non numquam eius modi tempora incidunt ut labore et dolore.</p>
    <ul class="checks">
      <li><svg width="16" height="12" viewBox="0 0 16 12"><path d="M1.5 6l4.5 4.5L14.5 1.5" stroke="#f7821b" stroke-width="2.4" fill="none"/></svg>More-or-less normal distribution of letters.</li>
      <li><svg width="16" height="12" viewBox="0 0 16 12"><path d="M1.5 6l4.5 4.5L14.5 1.5" stroke="#f7821b" stroke-width="2.4" fill="none"/></svg>Various versions have evolved over the years</li>
      <li><svg width="16" height="12" viewBox="0 0 16 12"><path d="M1.5 6l4.5 4.5L14.5 1.5" stroke="#f7821b" stroke-width="2.4" fill="none"/></svg>When an unknown printer took a galley</li>
    </ul>
  </div>
  <a class="btn">Read More <svg viewBox="0 0 16 16" fill="none" stroke="#fff" stroke-width="1.6"><circle cx="8" cy="8" r="7"/><path d="M5 8h6M8.5 5.5 11 8l-2.5 2.5"/></svg></a>
</section>

<section class="purpose">
  <h2>Our purpose</h2>
  <span class="bar"></span>
  <p>Voluptatem accusantium doloremque laudantium, totam rem aperiam eaque ipsa quae abist illo inventore veritatis et quasi architecto beatae vitae dictaphon sunt explicabo.</p>
</section>

<div class="card" style="left:92px;top:2392px">
  <svg class="icon" viewBox="0 0 66 66" fill="none" stroke="#1f4fb0" stroke-width="2"><path d="M18 12 33 5l15 7-15 7z"/><path d="M25 15v7a8 8 0 0 0 16 0v-7"/><rect x="10" y="34" width="46" height="22" rx="2"/><path d="M6 58h54" stroke="#f7821b"/><circle cx="33" cy="44" r="4" stroke="#f7821b"/></svg>
  <h3>School foundations</h3><span class="bar"></span>
  <p>Ut enim ad minim veniam uisop nostrud exercitation ullamcomosi laboris nisi ut aliquip.</p>
  <div class="more">Read More <svg width="15" height="15" viewBox="0 0 16 16" fill="none" stroke="#1f4fb0" stroke-width="1.6"><circle cx="8" cy="8" r="7"/><path d="M5 8h6M8.5 5.5 11 8l-2.5 2.5"/></svg></div>
</div>
<div class="card" style="left:437px;top:2392px">
  <svg class="icon" viewBox="0 0 66 66" fill="none" stroke="#1f4fb0" stroke-width="2"><ellipse cx="33" cy="33" rx="28" ry="11"/><ellipse cx="33" cy="33" rx="28" ry="11" transform="rotate(60 33 33)"/><ellipse cx="33" cy="33" rx="28" ry="11" transform="rotate(-60 33 33)"/><circle cx="33" cy="33" r="5" stroke="#f7821b"/></svg>
  <h3>Curriculum</h3><span class="bar"></span>
  <p>Ut enim ad minim veniam uisop nostrud exercitation ullamcomosi laboris nisi ut aliquip.</p>
  <div class="more">Read More <svg width="15" height="15" viewBox="0 0 16 16" fill="none" stroke="#1f4fb0" stroke-width="1.6"><circle cx="8" cy="8" r="7"/><path d="M5 8h6M8.5 5.5 11 8l-2.5 2.5"/></svg></div>
</div>
<div class="card" style="left:781px;top:2392px">
  <svg class="icon" viewBox="0 0 66 66" fill="none" stroke="#1f4fb0" stroke-width="2"><rect x="8" y="14" width="44" height="38" rx="3"/><circle cx="22" cy="30" r="5"/><path d="M13 46a9 9 0 0 1 18 0"/><path d="M42 22a7 7 0 1 1 0 0.1M40 32h5" stroke="#f7821b"/><path d="M44 4v4M54 9l-3 3M34 9l3 3" stroke="#f7821b"/></svg>
  <h3>Pedagogy</h3><span class="bar"></span>
  <p>Ut enim ad minim veniam uisop nostrud exercitation ullamcomosi laboris nisi ut aliquip.</p>
  <div class="more">Read More <svg width="15" height="15" viewBox="0 0 16 16" fill="none" stroke="#1f4fb0" stroke-width="1.6"><circle cx="8" cy="8" r="7"/><path d="M5 8h6M8.5 5.5 11 8l-2.5 2.5"/></svg></div>
</div>
<div class="card" style="left:92px;top:2805px">
  <svg class="icon" viewBox="0 0 66 66" fill="none" stroke="#1f4fb0" stroke-width="2"><circle cx="33" cy="12" r="5"/><path d="M22 18l11 8 11-8M33 26v18M26 60l7-16 7 16"/><path d="M10 50V34M6 38l4-4 4 4M56 50V34M52 38l4-4 4 4" stroke="#f7821b"/></svg>
  <h3>Outcomes</h3><span class="bar"></span>
  <p>Ut enim ad minim veniam uisop nostrud exercitation ullamcomosi laboris nisi ut aliquip.</p>
  <div class="more">Read More <svg width="15" height="15" viewBox="0 0 16 16" fill="none" stroke="#1f4fb0" stroke-width="1.6"><circle cx="8" cy="8" r="7"/><path d="M5 8h6M8.5 5.5 11 8l-2.5 2.5"/></svg></div>
</div>
<div class="card" style="left:437px;top:2805px">
  <svg class="icon" viewBox="0 0 66 66" fill="none" stroke="#1f4fb0" stroke-width="2"><rect x="8" y="14" width="42" height="40" rx="3"/><path d="M16 30h16M16 38h20M16 46h12"/><circle cx="46" cy="20" r="8" stroke="#f7821b"/><path d="M44 30h4M46 4v3M57 10l-2 2M35 10l2 2" stroke="#f7821b"/></svg>
  <h3>Opening</h3><span class="bar"></span>
  <p>Ut enim ad minim veniam uisop nostrud exercitation ullamcomosi laboris nisi ut aliquip.</p>
  <div class="more">Read More <svg width="15" height="15" viewBox="0 0 16 16" fill="none" stroke="#1f4fb0" stroke-width="1.6"><circle cx="8" cy="8" r="7"/><path d="M5 8h6M8.5 5.5 11 8l-2.5 2.5"/></svg></div>
</div>
<div class="donate" role="img" aria-label="Hands holding a red heart, donation appeal">
  <svg class="abs" style="left:14px;top:14px" width="300" height="368" viewBox="0 0 300 368" fill="none" stroke="#fff" stroke-width="3"><path d="M2 24V2h22"/><path d="M298 344v22h-22"/><rect x="6" y="28" width="8" height="8" fill="#f7821b" stroke="none"/><rect x="284" y="328" width="8" height="8" fill="#fff" stroke="none"/></svg>
  <div class="badge"><svg width="26" height="24" viewBox="0 0 26 24" fill="none" stroke="#1f4fb0" stroke-width="2"><rect x="2" y="8" width="22" height="14" rx="2"/><path d="M13 19s-4-2.5-4-5a2 2 0 0 1 4-0.5 2 2 0 0 1 4 .5c0 2.5-4 5-4 5z"/><circle cx="13" cy="4" r="3" fill="#f7821b" stroke="none"/></svg></div>
  <h3>For hold hands<br>together tight<br>donate us...</h3>
  <div class="give">Donate Now <svg width="15" height="15" viewBox="0 0 16 16" fill="none" stroke="#fff" stroke-width="1.6"><circle cx="8" cy="8" r="7"/><path d="M5 8h6M8.5 5.5 11 8l-2.5 2.5"/></svg></div>
</div>

<section class="statement">
  <h2 class="center-title" style="top:3300px">Statement of oneness with equity</h2>
  <span class="bar center-bar" style="top:3350px"></span>
  <p>Voluptatem accusantium doloremque laudantium, totam rem aperiam, eaque ipsa quae abist illo inventore veritatis et quasi architecto beatae vitae dictaphon sunt explicabo. Nemo enim ipsam voluptatem quia voluptas sit aspernatur auts onno.</p>
  <svg class="abs" style="left:80px;top:3550px" width="1040" height="440" viewBox="0 0 1040 440" fill="none" stroke-width="8" stroke-linecap="round">
    <path d="M14 90 A180 180 0 0 1 366 90" stroke="#f7821b"/>
    <path d="M344 330 A180 180 0 0 0 696 330" stroke="#1f4fb0"/>
    <path d="M674 90 A180 180 0 0 1 1026 90" stroke="#f7821b"/>
  </svg>
  <div class="ph" role="img" aria-label="Three smiling children hugging" style="left:96px;top:3596px;width:340px;height:340px;border-radius:50%;background:radial-gradient(circle at 50% 40%,#e7c9b4,#c79a82 55%,#9a7466)"></div>
  <div class="ph" role="img" aria-label="Pink blossoms on a branch" style="left:432px;top:3596px;width:336px;height:336px;border-radius:50%;background:radial-gradient(circle at 50% 50%,#e59abb,#8da36a 60%,#4f6b3a)"></div>
  <div class="ph" role="img" aria-label="Happy family outdoors with a child on a parent's shoulders" style="left:764px;top:3596px;width:340px;height:340px;border-radius:50%;background:radial-gradient(circle at 50% 40%,#f0c98a,#d19a4e 55%,#8f5e2c)"></div>
</section>

<section class="testimonials">
  <h2>What our<br>learners says</h2>
  <span class="bar"></span>
  <div class="arrow" style="left:972px;background:#dde4f1"><svg width="20" height="16" viewBox="0 0 20 16"><path d="M18 8H2M8 2 2 8l6 6" stroke="#1f4fb0" stroke-width="2" fill="none"/></svg></div>
  <div class="arrow" style="left:1046px;background:var(--blue)"><svg width="20" height="16" viewBox="0 0 20 16"><path d="M2 8h16M12 2l6 6-6 6" stroke="#fff" stroke-width="2" fill="none"/></svg></div>
  <div class="quote" style="left:92px">
    <div class="mark">”</div>
    <div class="avatar" role="img" aria-label="Portrait of learner Maya Rivers" style="background:linear-gradient(160deg,#d9b8a6,#8b5e4e)"></div>
    <p>sed do eiusmod tempor incididunt ut labore etenis dolore magna aliqua. Ut enim ad minim veniam quis nostrud exercitation ullamcoinventore veritatis..</p>
    <h4>Maya Rivers</h4><span>Student</span>
  </div>
  <div class="quote" style="left:612px">
    <div class="mark">”</div>
    <div class="avatar" role="img" aria-label="Portrait of learner Nora Castell" style="background:linear-gradient(160deg,#e9c86a,#8a6fc0)"></div>
    <p>sed do eiusmod tempor incididunt ut labore etenis dolore magna aliqua. Ut enim ad minim veniam quis nostrud exercitation ullamcoinventore veritatis..</p>
    <h4>Nora Castell</h4><span>Student</span>
  </div>
</section>

<footer class="footer">
  <div class="mark-name">Lumen Grove<br>School</div>
  <div class="socials" aria-label="Social links"><span></span><span></span><span></span></div>
  <h4 style="left:426px;top:78px">Quick links</h4>
  <span class="fbar" style="left:426px;top:112px"></span>
  <ul style="left:426px;top:146px"><li>About</li><li>School Foundations</li><li>Curriculum</li><li>Pedagogy</li></ul>
  <ul style="left:632px;top:146px"><li>Outcome</li><li>Opening</li><li>Testimonials</li><li>Donate</li></ul>
  <h4 style="left:882px;top:78px">Contact info</h4>
  <span class="fbar" style="left:882px;top:112px"></span>
  <div class="contact" style="top:140px">
    <svg width="16" height="16" viewBox="0 0 24 24" fill="#f7821b"><path d="M22 16.9v3a2 2 0 0 1-2.2 2 19.8 19.8 0 0 1-8.6-3.1 19.5 19.5 0 0 1-6-6A19.8 19.8 0 0 1 2.1 4.2 2 2 0 0 1 4.1 2h3a2 2 0 0 1 2 1.7c.1 1 .4 1.9.7 2.8a2 2 0 0 1-.5 2.1L8 9.8a16 16 0 0 0 6 6l1.3-1.3a2 2 0 0 1 2.1-.4c.9.3 1.8.6 2.8.7a2 2 0 0 1 1.7 2z"/></svg>
    <div>Phone no:<br>555-014-2368</div>
  </div>
  <div class="contact" style="top:232px">
    <svg width="18" height="16" viewBox="0 0 18 16" fill="#f7821b"><path d="M1 6 9 1l8 5v9H1z"/></svg>
    <div>Email:<br>hello@lumengrove.org</div>
  </div>
  <div class="copyright">Copyright © 2023 Lumen Grove School. All rights reserved.</div>
</footer>

</body>
</html>
```